Travel / Surf Shop Brochure

We are running a surf shop and also we are organising surf and multi-sport (bike, longboard, kaiak) trips in summer.
We need a concise well designed brochure to promote our trips (max 4 activities) and also our shop (maybe including few featured products).
We want to keep our production cost low, so a folded brochure would be good start for us.
As an idea you can review our Facebook profile (https://www.facebook.com/tidelark.store), see the photos, etc.
I can provide any photo from there in good resolution.
The surf destination is Portugal, so you can use any blow-mind pic of this destination.
When I'm first looking this brochure I have to think "I NEED IT, I WANT TO GO THERE". The look and feel should be around the the idea of well-being and outdoor entertainment.
The texts will NOT be in english so for the moment you can use some ample or english texts.
Updates
The logo is uploaded.
Please contact me for any requests or questions.
New pictures are uploaded.
Target Market(s)
We are talking with young and mature public, 25-35 years old, active pople.
Industry/Entity Type
Shop
Look and feel

```html
<!DOCTYPE html>
<html lang="ro">
<head>
<meta charset="utf-8">
<title>Tidelark — Surf Shop Brochure</title>
<link rel="stylesheet" href="https://fonts.googleapis.com/css2?family=Roboto+Condensed:ital,wght@0,400;0,700;0,800;1,400&family=PT+Sans:ital,wght@0,400;0,700;1,400&display=swap">
<style>
  :root{
    --yellow:#ffe100;
    --pink:#e8175d;
    --cyan:#27b5e6;
    --ink:#2a2320;
    --white:#ffffff;
    --paper:#ffffff;
  }
  *{box-sizing:border-box;margin:0;padding:0}
  html,body{width:1200px;height:927px;overflow:hidden;background:var(--paper)}
  .canvas{position:relative;width:1200px;height:927px;background:var(--paper);font-family:"PT Sans",sans-serif}
  .panel{position:absolute;overflow:hidden}
  .photo{position:absolute;display:block}
  .display{font-family:"Roboto Condensed",sans-serif;font-weight:800;text-transform:uppercase;letter-spacing:-0.5px;line-height:1}
  .copy{font-family:"PT Sans",sans-serif;font-size:9.5px;line-height:1.3}

  .label{position:absolute;display:flex;align-items:center;padding-left:10px}
  .label--arrow{clip-path:polygon(0 0,100% 0,88% 50%,100% 100%,0 100%)}

  /* Top spread */
  .cover-left{left:543px;top:0;width:215px;height:463px}
  .cover-left .photo{inset:0;background:linear-gradient(180deg,#3aa9d8 0%,#7fb7d3 35%,#4d79a8 60%,#2d5580 100%)}
  .cover-left .intro{position:absolute;left:0;top:0;width:215px;min-height:204px;background:var(--pink);padding:68px 8px 10px 12px;color:var(--white)}
  .cover-left .intro-heading{left:12px;top:22px;width:170px;height:42px;background:var(--yellow);color:var(--ink);font-size:33px}

  .cover-mid{left:758px;top:0;width:222px;height:463px;background:var(--yellow)}
  .cover-mid .photo{left:0;top:0;width:222px;height:109px;background:linear-gradient(90deg,#3e8f95,#7fa3a0 50%,#2e6e7a)}
  .cover-mid .kicker{position:absolute;left:8px;top:114px;width:210px;color:var(--ink)}
  .cover-mid .kicker strong{display:block;font-size:10px;font-weight:700;text-transform:uppercase}
  .cover-mid .kicker em{display:block;font-size:9.5px;line-height:1.25}
  .cover-mid .headline{position:absolute;left:6px;top:172px;width:214px;color:var(--ink);font-size:50px;font-weight:700;line-height:0.82;letter-spacing:-2px}
  .cover-mid .contact{position:absolute;left:8px;top:419px;font-size:9px;font-weight:700;color:var(--ink);white-space:nowrap;letter-spacing:-0.2px}

  .cover-right{left:980px;top:0;width:220px;height:463px}
  .cover-right .photo{inset:0;background:linear-gradient(160deg,#d7c6a8 0%,#b39a7c 45%,#7a6a5c 75%,#4a413b 100%)}
  .brand{position:absolute;left:0;top:0;width:220px;height:50px;background:var(--cyan);display:flex;align-items:center;justify-content:center}
  .brand-name{font-family:"Roboto Condensed",sans-serif;font-weight:800;font-size:40px;color:var(--white);letter-spacing:-0.5px}
  .brand-tag{position:absolute;left:0;width:220px;top:78px;text-align:center;font-size:11px;font-weight:700;color:var(--ink)}
  .sports{list-style:none}
  .sports .label{left:0;font-size:32px}
  .sport--surf{top:265px;width:100px;height:41px;background:var(--cyan);color:var(--ink)}
  .sport--board{top:311px;width:140px;height:41px;background:var(--yellow);color:var(--ink)}
  .sport--ride{top:355px;width:112px;height:38px;background:var(--pink);color:var(--ink)}
  .sport--kaiak{top:396px;width:130px;height:39px;background:var(--ink);color:var(--yellow);clip-path:none}

  /* Bottom spread */
  .inside-left{left:543px;top:465px;width:221px;height:462px}
  .inside-left .photo{left:0;top:0;width:221px;height:356px;background:linear-gradient(180deg,#d29a2a 0%,#c7b23a 40%,#b06a2e 75%,#6b3c63 100%)}
  .flag{position:absolute;left:0;top:51px;width:140px;height:33px;display:flex}
  .flag-name{flex:1;background:var(--cyan);display:flex;align-items:center;justify-content:center;font-family:"Roboto Condensed",sans-serif;font-weight:800;font-size:22px;color:var(--white);clip-path:polygon(0 0,100% 0,100% 100%,0 100%,10% 50%)}
  .inside-left .story{position:absolute;left:0;top:356px;width:221px;height:106px;background:var(--yellow);padding:7px 8px;color:var(--ink)}

  .inside-mid{left:764px;top:465px;width:221px;height:462px}
  .inside-mid .photo{left:0;top:0;width:221px;height:273px;background:linear-gradient(135deg,#2a4a2a 0%,#6b3a2a 40%,#1e2a55 75%,#3a3a3a 100%)}
  .inside-mid .h1{top:186px;left:0;width:190px;height:38px;background:var(--yellow);color:var(--ink);font-size:32px}
  .inside-mid .h2{top:230px;left:0;width:205px;height:40px;background:var(--pink);color:var(--ink);font-size:32px}
  .inside-mid .body{position:absolute;left:0;top:273px;width:221px;height:189px;background:var(--cyan);padding:8px 8px;color:var(--white)}
  .inside-mid .body p+p{margin-top:10px}

  .inside-right{left:985px;top:465px;width:215px;height:462px}
  .inside-right .photo{left:0;top:0;width:215px;height:272px;background:linear-gradient(90deg,#3a6b6e 0%,#c33a4a 35%,#2e5a66 60%,#d9d0c5 100%)}
  .inside-right .shop-heading{top:269px;left:0;width:110px;height:38px;background:var(--yellow);color:var(--ink);font-size:32px}
  .inside-right .body{position:absolute;left:0;top:307px;width:215px;height:155px;background:var(--pink);padding:8px 6px;color:var(--white)}
</style>
</head>
<body>
<main class="canvas">

  <section class="panel cover-left">
    <div class="photo" role="img" aria-label="Close-up photo of a person in faded denim jeans with a red plaid belt"></div>
    <div class="intro">
      <h2 class="label label--arrow intro-heading display">Heading</h2>
      <p class="copy">Rum que volore prerum fugitat quatem ini quia perum facea dolore ea aut re porion con es deliae ne nustiunt accae voluptatia dolores sinvendebita pernatquas reperis eiur si veliti ommos resti in consent lantior rovite sae verspid eium aboria abor ad ut offic tem fugiatia dis maion consequodit fugitatur? Dante sit moluptatis digenducid explias es dolluptam ute voluptaqui ratem et excepta sperios ut</p>
    </div>
  </section>

  <section class="panel cover-mid">
    <div class="photo" role="img" aria-label="Photo of three young women in swimwear by a pool"></div>
    <div class="kicker">
      <strong>Deci vii in Hangar</strong>
      <em>Deci vii in Hangar in primul ca sa ne cunoastem si sa discutam despre bike, kite, wake, skate. Pentru ca</em>
    </div>
    <h1 class="headline display">It’s only about passion, love and fun.</h1>
    <p class="contact">contact@tidelark.store | www.tidelarkshop.com</p>
  </section>

  <section class="panel cover-right">
    <div class="photo" role="img" aria-label="Photo of a young couple in sunglasses and printed t-shirts"></div>
    <div class="brand"><span class="brand-name">TIDELARK</span></div>
    <p class="brand-tag">SKI &amp; SURF SHOP</p>
    <ul class="sports">
      <li class="label label--arrow display sport--surf">Surf</li>
      <li class="label label--arrow display sport--board">Board</li>
      <li class="label label--arrow display sport--ride">Ride</li>
      <li class="label display sport--kaiak">Kaiak</li>
    </ul>
  </section>

  <section class="panel inside-left">
    <div class="photo" role="img" aria-label="Photo of a frosted cupcake in a striped wrapper with a small shop flag"></div>
    <div class="flag"><span class="flag-name">TIDELARK</span></div>
    <p class="story copy">este magazinul in care vanzatorii iti sunt in primul rand prieteni si colegi de dat, in care cel mai de valoare “asset” este sfatul pertinent venit de la niste oameni care chiar practica sporturile pe care le promoveaza si care chiar folosesc produsele pe care le vand.</p>
  </section>

  <section class="panel inside-mid">
    <div class="photo" role="img" aria-label="Photo of a shop counter with a bottle, goggles and colourful gear"></div>
    <h2 class="label label--arrow display h1">Heading</h2>
    <h3 class="label label--arrow display h2">Heading 2</h3>
    <div class="body copy">
      <p>Rum que volore prerum fugitat quatem ini quia perum facea dolore ea aut re porion con es deliae ne nustiunt accae voluptatia dolores sinvendebita pernatquas reperis eiur si veliti ommos resti in consent lantior rovite sae verspid eium aboria abor ad ut offic tem fugiatia dis maion consequodit fugitatur? Dante sit moluptatis digenducid explias es dolluptam ute voluptaqui ratem et excepta sperios ut</p>
      <p>Rum que volore prerum fugitat quatem ini quia perum facea dolore ea aut re porion con es deliae</p>
    </div>
  </section>

  <section class="panel inside-right">
    <div class="photo" role="img" aria-label="Photo of snowboards on a shop rack with a sale tag"></div>
    <h2 class="label label--arrow display shop-heading">Shop</h2>
    <p class="body copy">Rum que volore prerum fugitat quatem ini quia perum facea dolore ea aut re porion con es deliae ne nustiunt accae voluptatia dolores sinvendebita pernatquas reperis eiur si veliti ommos resti in consent lantior rovite sae verspid eium aboria abor ad ut offic tem fugiatia dis maion consequodit fugitatur? Dante sit moluptatis digenducid explias es dolluptam ute voluptaqui ratem et excepta sperios ut</p>
  </section>

</main>
</body>
</html>
```